Brivane - Business Cards for a new venture

create business card for a startup classified business dealing in construction materials, the cards need to have a professional look but modern, more serious than playful, one of the samples must include the official font (attached), please explore using the official colors in the company's logo

Target Market(s)

Energy sector

Contact Information for Business Card

Font styles to use
Other font styles liked:
• suissnord

Requirements
Must have
• corporate colors (in logo attached)
Nice to have
• Official font (in one of the samples) font is : suissnord
Should not have
• Cartoonish look

```html
<!DOCTYPE html>
<html lang="en">
<head>
<meta charset="utf-8">
<title>Brivane – Business Cards</title>
<link href="https://fonts.googleapis.com/css2?family=Michroma&display=swap" rel="stylesheet">
<style>
  :root {
    --navy: #144679;
    --navy-deep: #0f3a66;
    --grey: #9a9b9d;
    --grey-light: #b4b5b7;
    --paper: #ffffff;
    --stage: #e6e7e9;
  }
  * { margin: 0; padding: 0; box-sizing: border-box; }
  html, body { width: 1200px; height: 1040px; overflow: hidden; }
  body {
    background: var(--stage);
    font-family: "Michroma", sans-serif;
    position: relative;
  }
  .card {
    position: absolute;
    width: 700px;
    height: 400px;
    box-shadow: 0 10px 30px rgba(0,0,0,0.18);
    overflow: hidden;
  }
  /* Front */
  .card-front {
    left: 60px; top: 60px;
    background: var(--navy);
    color: var(--paper);
    display: flex;
    flex-direction: column;
    align-items: center;
    justify-content: center;
    gap: 34px;
  }
  .brand {
    display: flex;
    align-items: center;
    gap: 18px;
    letter-spacing: 0.22em;
    text-transform: uppercase;
  }
  .brand-mark { width: 18px; height: 18px; background: currentColor; }
  .card-front .brand { font-size: 40px; }
  .front-web { font-size: 15px; letter-spacing: 0.08em; }

  /* Back */
  .card-back {
    left: 440px; top: 580px;
    background: var(--paper);
  }
  .card-back .brand {
    position: absolute;
    right: 52px; top: 64px;
    font-size: 26px;
    color: var(--grey);
  }
  .card-back .brand-mark { width: 14px; height: 14px; background: var(--navy); }
  .holder { position: absolute; left: 46px; top: 168px; }
  .holder-name { font-size: 20px; color: var(--navy); letter-spacing: 0.06em; }
  .holder-role { font-size: 12px; color: var(--grey); letter-spacing: 0.12em; margin-top: 4px; }
  .address {
    margin-top: 20px;
    font-size: 11px;
    line-height: 1.55;
    color: var(--navy);
  }
  .contacts { list-style: none; margin-top: 12px; }
  .contacts li {
    display: flex; align-items: center; gap: 10px;
    font-size: 11px; line-height: 1.9; color: var(--grey);
  }
  .contacts svg { width: 14px; height: 14px; fill: var(--navy); flex: none; }
  .band {
    position: absolute; left: 0; right: 0; bottom: 0;
    height: 22px; display: flex;
  }
  .band-navy { flex: 0 0 72%; background: var(--navy); }
  .band-grey { flex: 1; background: var(--grey-light); }
</style>
</head>
<body>
  <section class="card card-front">
    <div class="brand"><span class="brand-mark"></span>Brivane</div>
    <div class="front-web">www.lenaharwick.com</div>
  </section>

  <section class="card card-back">
    <div class="brand"><span class="brand-mark"></span>Brivane</div>

    <div class="holder">
      <div class="holder-name">LENA HARWICK</div>
      <div class="holder-role">FOUNDER</div>
      <div class="address">Maple Grove Street No,<br>Zip Code, State, MG-456, Norbury</div>
      <ul class="contacts">
        <li>
          <svg viewBox="0 0 24 24" aria-hidden="true"><path d="M6.6 10.8a15 15 0 0 0 6.6 6.6l2.2-2.2a1 1 0 0 1 1-.25 11.4 11.4 0 0 0 3.6.6 1 1 0 0 1 1 1V20a1 1 0 0 1-1 1A17 17 0 0 1 3 4a1 1 0 0 1 1-1h3.5a1 1 0 0 1 1 1c0 1.25.2 2.45.6 3.6a1 1 0 0 1-.25 1z"/></svg>
          (555) 310-0000
        </li>
        <li>
          <svg viewBox="0 0 24 24" aria-hidden="true"><path d="M7 1h10a2 2 0 0 1 2 2v18a2 2 0 0 1-2 2H7a2 2 0 0 1-2-2V3a2 2 0 0 1 2-2zm0 3v14h10V4zm5 15.2a1.2 1.2 0 1 0 0 2.4 1.2 1.2 0 0 0 0-2.4z"/></svg>
          (555) 320-0000
        </li>
        <li>
          <svg viewBox="0 0 24 24" aria-hidden="true"><path d="M2 5h20v14H2zm2 2v.5l8 5 8-5V7zm0 2.8V17h16V9.8l-8 5z"/></svg>
          lena@harwick.com
        </li>
        <li>
          <svg viewBox="0 0 24 24" aria-hidden="true"><path d="M12 2a10 10 0 1 0 0 20 10 10 0 0 0 0-20zm6.9 9h-3a15 15 0 0 0-1.3-5.7A8 8 0 0 1 18.9 11zM12 4c.9 1.2 1.8 3.6 1.9 7h-3.8c.1-3.4 1-5.8 1.9-7zM9.4 5.3A15 15 0 0 0 8.1 11h-3a8 8 0 0 1 4.3-5.7zM5.1 13h3a15 15 0 0 0 1.3 5.7A8 8 0 0 1 5.1 13zM12 20c-.9-1.2-1.8-3.6-1.9-7h3.8c-.1 3.4-1 5.8-1.9 7zm2.6-1.3a15 15 0 0 0 1.3-5.7h3a8 8 0 0 1-4.3 5.7z"/></svg>
          www.lenaharwick.com
        </li>
      </ul>
    </div>

    <div class="band"><div class="band-navy"></div><div class="band-grey"></div></div>
  </section>
</body>
</html>
```